Book Cover - For Best Selling Diet

Hi
Book cover required for a diet book being marketed to become a best seller
For best quality, image will be 2820 pixels on the shortest side and 4500 pixels on the longest side .
The book name : Bright Morning Plan
By Marisol Penhale
( will add in the extra text once we see design - top and bottom subtitle )
I do not want a photo of a person on the book.
PLEASE SEE " THE NINE STEP CORE" by Dale Whitcombe as an example of solid style and I also love Quiet Lantern for the font.
Branding Colours:
#F26432
#A4195C
#A7D8CC
Font that runs through our brand is : helvetica neue
This is for a book that will be marketed for #1 bestseller - So please only quality
designs that are designed in a unique style.
Thanks
Target Market(s)
Busy Working Mums, Affluent, 30+ .
Look and feel

```html
<!DOCTYPE html>
<html lang="en">
<head>
<meta charset="utf-8">
<title>Bright Morning Plan — Marisol Penhale</title>
<link rel="stylesheet" href="https://fonts.googleapis.com/css2?family=Inter:wght@200;300&display=swap">
<style>
  :root {
    --brand-orange: #F26432;
    --brand-berry: #A4195C;
    --brand-mint: #A7D8CC;
    --berry-deep: #7a0f44;
    --type: #ffffff;
  }
  * { margin: 0; padding: 0; box-sizing: border-box; }
  html, body {
    width: 760px;
    height: 1200px;
    overflow: hidden;
    background: var(--brand-berry);
  }
  .cover {
    position: relative;
    width: 760px;
    height: 1200px;
    overflow: hidden;
    background: linear-gradient(to bottom left,
      var(--berry-deep) 0%,
      var(--brand-berry) 45%,
      var(--brand-orange) 100%);
    font-family: "Inter", "Helvetica Neue", Helvetica, Arial, sans-serif;
    color: var(--type);
  }
  .vine-artwork {
    position: absolute;
    left: 22px;
    top: 18px;
    width: 100px;
    height: 1164px;
    border-radius: 50px;
    background: linear-gradient(to bottom,
      var(--brand-mint) 0%,
      var(--brand-orange) 25%,
      var(--brand-mint) 50%,
      var(--brand-orange) 75%,
      var(--brand-mint) 100%);
    opacity: 0.8;
  }
  .book-title {
    position: absolute;
    left: 150px;
    right: 10px;
    top: 18px;
    text-align: center;
    font-weight: 200;
    font-size: 124px;
    line-height: 244px;
    letter-spacing: 0.01em;
    text-transform: uppercase;
  }
  .book-title span { display: block; }
  .book-author {
    position: absolute;
    right: 46px;
    bottom: 56px;
    font-weight: 300;
    font-size: 58px;
    letter-spacing: -0.01em;
    white-space: nowrap;
  }
</style>
</head>
<body>
  <main class="cover">
    <div class="vine-artwork" role="img" aria-label="Climbing vine with a thin dark stem and mint and orange leaves running up the left edge"></div>
    <h1 class="book-title">
      <span>Bright</span>
      <span>Morning</span>
      <span>Plan</span>
    </h1>
    <p class="book-author">Marisol Penhale</p>
  </main>
</body>
</html>
```